Vape case graphic design

We are looking to create unique design with pattern prints for our Vape case.

The appearance is required to be dynamic and layered, also our theme is related to ice, we need the ice feeling. And we need the design which is matched with European and America style.

We attached our Vape case size and shape for your reference. Pls put your design on the vape case, not just give us the plain design artwork.

Target Market(s)

European and American market

Industry/Entity Type

Vape

```html
<!DOCTYPE html>
<html lang="en">
<head>
<meta charset="utf-8">
<title>K&amp;V Frost 5000 – Packaging Artwork</title>
<link rel="stylesheet" href="https://fonts.googleapis.com/css2?family=Montserrat:wght@500;600;700&display=swap">
<style>
  :root {
    --page-bg: #f3f5f7;
    --brand-blue: #0a96d6;
    --brand-blue-deep: #0b6fa8;
    --side-navy: #0b4680;
    --side-navy-deep: #082c55;
    --ice-frost: #d6ecf8;
    --ice-light: #a9d3ec;
    --ice-mid: #5fa4cf;
    --ice-deep: #1f5f8f;
    --ice-shadow: #174e78;
    --accent-orange: #e0500e;
    --device-dark: #2a2f3a;
    --text-white: #f4f6f8;
  }
  html, body {
    margin: 0;
    padding: 0;
    width: 1200px;
    height: 1084px;
    overflow: hidden;
    background: var(--page-bg);
  }
  .artwork {
    display: block;
    width: 1200px;
    height: 1084px;
  }
  .brand-name,
  .product-name,
  .flavour-label {
    font-family: "Montserrat", sans-serif;
    fill: var(--text-white);
  }
  .brand-name { font-weight: 700; font-size: 70px; }
  .product-name { font-weight: 600; font-size: 52px; }
  .flavour-label { font-weight: 700; font-size: 40px; }
  .flavour-strength { font-weight: 500; }
</style>
</head>
<body>
<svg class="artwork" viewBox="0 0 1200 1084" xmlns="http://www.w3.org/2000/svg">
  <defs>
    <linearGradient id="ice-base" x1="0" y1="0" x2="0" y2="1">
      <stop offset="0" stop-color="var(--ice-mid)"/>
      <stop offset="0.35" stop-color="var(--ice-deep)"/>
      <stop offset="0.6" stop-color="var(--ice-shadow)"/>
      <stop offset="0.8" stop-color="var(--ice-mid)"/>
      <stop offset="1" stop-color="var(--ice-light)"/>
    </linearGradient>
    <radialGradient id="ice-glare" cx="0.15" cy="0.3" r="0.45">
      <stop offset="0" stop-color="var(--ice-frost)" stop-opacity="0.75"/>
      <stop offset="1" stop-color="var(--ice-frost)" stop-opacity="0"/>
    </radialGradient>
    <radialGradient id="ice-pile" cx="0.5" cy="1" r="0.7">
      <stop offset="0" stop-color="var(--ice-frost)" stop-opacity="0.95"/>
      <stop offset="0.6" stop-color="var(--ice-light)" stop-opacity="0.7"/>
      <stop offset="1" stop-color="var(--ice-light)" stop-opacity="0"/>
    </radialGradient>
    <linearGradient id="header-fill" x1="0" y1="0" x2="1" y2="1">
      <stop offset="0" stop-color="var(--brand-blue-deep)"/>
      <stop offset="0.5" stop-color="var(--brand-blue)"/>
      <stop offset="1" stop-color="var(--brand-blue-deep)"/>
    </linearGradient>
    <linearGradient id="side-fill" x1="0" y1="0" x2="0" y2="1">
      <stop offset="0" stop-color="var(--side-navy-deep)"/>
      <stop offset="0.55" stop-color="var(--side-navy)"/>
      <stop offset="0.8" stop-color="var(--ice-deep)"/>
      <stop offset="1" stop-color="var(--ice-light)"/>
    </linearGradient>
  </defs>

  <!-- Front panel -->
  <g class="front-panel">
    <g class="ice-backdrop" role="img" aria-label="Photographic backdrop of cracked ice with a heap of ice cubes along the bottom">
      <rect x="380" y="180" width="360" height="720" fill="url(#ice-base)"/>
      <rect x="380" y="300" width="360" height="320" fill="url(#ice-glare)"/>
      <rect x="380" y="690" width="360" height="210" fill="url(#ice-pile)"/>
    </g>
    <polygon class="header-band" points="380,180 740,180 740,430 380,340" fill="url(#header-fill)"/>
    <text class="brand-name" x="408" y="272">K&amp;V</text>
    <text class="product-name" x="408" y="350" textLength="296" lengthAdjust="spacingAndGlyphs">FROST 5000</text>
    <line class="accent-rule" x1="426" y1="371" x2="688" y2="377"
          stroke="var(--accent-orange)" stroke-width="10" stroke-linecap="round"/>
    <path class="device-window"
          d="M482 425 H548 Q556 425 556 433 V447 Q556 455 564 455 H663 Q675 455 675 467 V773 Q675 785 663 785 H460 Q448 785 448 773 V467 Q448 455 460 455 H466 Q470 455 470 447 V437 Q470 425 482 425 Z"
          fill="var(--device-dark)"
          role="img" aria-label="Dark vape device seen through the display window"/>
  </g>

  <!-- Side panel -->
  <g class="side-panel">
    <rect x="740" y="180" width="100" height="720" fill="url(#side-fill)"/>
    <rect class="ice-base" x="740" y="700" width="100" height="200" fill="url(#ice-pile)"
          role="img" aria-label="Ice cubes continuing from the front panel"/>
    <rect class="flavour-tag" x="764" y="338" width="50" height="338" rx="14" fill="var(--accent-orange)"/>
    <text class="flavour-label" transform="rotate(90 775 245)" x="775" y="245" textLength="100" lengthAdjust="spacingAndGlyphs">MIX</text>
    <text class="flavour-label" transform="rotate(90 775 360)" x="775" y="360" textLength="290" lengthAdjust="spacingAndGlyphs">BERRIES <tspan class="flavour-strength">5%</tspan></text>
  </g>
</svg>
</body>
</html>
```